Sole trader needs a stationery design

We are a sole trader competing in government and tertiary education tenders. We require stationery design to appear more professional than our previous Quarnell standard template.

Our new logo is attached.

Please feel free to add and adjust colours.

Please provide detail on the fonts you are using.

The uploaded font is Tex Gyre Adventor. It is the font of the logo.

Company Details:
Pebblewick IT

My details are as follows:
Name: Dominic Valtrane
Role: Front end web consultant
Work: 02 7314 2286
Mobile: 0418 652 307
Address: not required
Email: dvaltrane@mailbrook.example
Website: http://www.pebblewickit.example.au

Target Market(s)

Government and tertiary institutions

Industry/Entity Type

Information Technology

Font styles to use
Sans Serif

Requirements
Must have
• We require the following stationery design:
• - Business cards
• - Physical letterhead
• - Tender document with coverpage and appendix coverpage
• - Internal tender page
• Content copy items to include:
• - Table
• - Image with caption (figure)
• - Figure text
• - Table of contents
• - Headings (up to 5 levels)
• - Paragraph with bold / italic text
• - Hyperlink
• - Ordered list
• - Bullet list
Should not have
• Serif fonts

```html
<!DOCTYPE html>
<html lang="en">
<head>
<meta charset="utf-8">
<title>Pebblewick IT – Tender Page</title>
<link rel="stylesheet" href="https://fonts.googleapis.com/css2?family=Questrial&family=Montserrat:wght@500;700&display=swap">
<style>
  :root{
    --blue:#1a8fd6;
    --blue-dark:#0f67a8;
    --ink:#2b2b2b;
    --ink-soft:#555;
    --paper:#ffffff;
    --rule:#1a8fd6;
  }
  *{box-sizing:border-box;margin:0;padding:0}
  html,body{width:878px;height:1200px;overflow:hidden;background:var(--paper)}
  .page{position:relative;width:878px;height:1200px;background:var(--paper);font-family:"Questrial",sans-serif;color:var(--ink)}

  .brand{position:absolute;left:64px;top:62px;display:flex;align-items:center;gap:12px}
  .brand-square{width:34px;height:34px;background:var(--blue)}
  .brand-name{font-family:"Montserrat",sans-serif;font-weight:700;font-size:36px;color:var(--blue-dark);letter-spacing:-0.5px}
  .brand-tag{position:absolute;left:110px;top:106px;font-size:10px;letter-spacing:2.5px;color:var(--ink-soft)}

  .corner{position:absolute;right:0;top:0}
  .contact{position:absolute;right:40px;top:56px;text-align:right}
  .contact-name{font-family:"Montserrat",sans-serif;font-weight:700;font-size:20px;color:var(--blue)}
  .contact-role{font-family:"Montserrat",sans-serif;font-weight:700;font-size:11px;color:var(--ink);margin-top:2px}
  .contact-line{font-size:9.5px;color:var(--ink);margin-top:3px}
  .contact-line b{color:var(--blue);font-weight:400}

  .title{position:absolute;top:262px;left:0;width:100%;text-align:center;font-family:"Montserrat",sans-serif;font-weight:700;font-size:32px;letter-spacing:0.5px;color:var(--ink)}

  .content{position:absolute;left:92px;top:340px;width:700px;font-size:17px;line-height:1.32;text-align:justify}
  .content p{margin-bottom:14px}
  .bullets{list-style:none}
  .bullets li{position:relative;padding-left:22px;margin-bottom:14px}
  .bullets li::before{content:"";position:absolute;left:2px;top:7px;width:8px;height:8px;background:var(--blue)}
  .sub{margin:10px 0 0 0}
  .sub-num{color:var(--blue);font-family:"Montserrat",sans-serif;font-weight:700}
  .content strong{font-family:"Montserrat",sans-serif;font-weight:500}

  .chart{position:absolute;left:150px;top:812px}
  .fig-caption{position:absolute;left:548px;top:978px;font-family:"Montserrat",sans-serif;font-weight:700;font-size:14px;color:var(--blue);text-decoration:underline}

  .footer-mark{position:absolute;left:98px;top:996px;width:20px;height:20px;background:var(--blue)}
  .footer-band{position:absolute;left:0;right:0;top:1030px;height:22px;background:var(--blue)}
  .page-no{position:absolute;right:0;top:1064px;width:150px;height:28px;background:var(--blue);color:#fff;font-family:"Montserrat",sans-serif;font-weight:700;font-size:14px;display:flex;align-items:center;padding-left:46px}
</style>
</head>
<body>
<div class="page">
  <div class="brand">
    <span class="brand-square"></span>
    <span class="brand-name">Pebblewick IT</span>
  </div>
  <div class="brand-tag">WEB CONSULTING SERVICES</div>

  <svg class="corner" width="200" height="50" viewBox="0 0 200 50">
    <polygon points="40,0 200,0 200,14 120,50" fill="var(--blue)"/>
  </svg>
  <div class="contact">
    <div class="contact-name">Dominic Valtrane</div>
    <div class="contact-role">FRONT END WEB CONSULTANT</div>
    <div class="contact-line"><b>Work Phone:</b> 02 7314 2286 &nbsp;|&nbsp; <b>Mobile:</b> 0418 652 307</div>
    <div class="contact-line"><b>Email:</b> dvaltrane@mailbrook.example &nbsp;|&nbsp; <b>www.pebblewickit.example.au</b></div>
  </div>

  <h1 class="title">INTRODUCTION</h1>

  <div class="content">
    <p>Procurement for works under public-financed projects is carried out in accordance with policies and procedures laid down in The Public Procurement and Disposal Act 2005 and The Public Procurement and Disposal Regulations 2006.</p>
    <ul class="bullets">
      <li>This SBD is mandatory for use in works contracts of a value not exceeding KShs.200 million, as defined in The Public Procurement and Disposal Act 2005 and The Public Procurement and Disposal Regulations 2006.</li>
      <li>Information contained in the Invitation for Tenders shall conform to the data and information in the Tender documents to enable prospective Tenderers to decide whether or not to participate in the Tender and shall indicate any important Tender requirements;
        <p class="sub"><span class="sub-num">1.1</span> Cost of documents: <em>(insert the currency and amount to cover cost of copying and binding only to a maximum of KShs.5,000)</em>. Payment should either be by Cash, Banker’s Draft, or Banker’s Cheque, payable to <em>(state organ to which payments are to be made)</em>.</p>
        <p class="sub"><span class="sub-num">1.2</span> All Tenders in accordance with the instructions to tenderers must be delivered to <strong>(insert physical address)</strong> at or before <strong>(insert time and date)</strong>.</p>
      </li>
      <li>The Invitation for Tenders shall be as an advertisement in accordance with the regulations or a letter of invitation addressed to Tenderers who have been prequalified following a request for prequalification.</li>
    </ul>
  </div>

  <svg class="chart" width="420" height="210" viewBox="0 0 420 210" font-family="Montserrat, sans-serif" font-size="7" fill="#222">
    <g transform="translate(180,95) scale(1.35,0.5)" stroke="#fff" stroke-width="0.8">
      <path d="M0 0 L0 -100 A100 100 0 0 1 96.9 -24.9 Z" fill="#7b1a1a"/>
      <path d="M0 0 L96.9 -24.9 A100 100 0 0 1 93.0 36.8 Z" fill="#2e7d5b"/>
      <path d="M0 0 L93.0 36.8 A100 100 0 0 1 68.5 72.9 Z" fill="#e4e4e4"/>
      <path d="M0 0 L68.5 72.9 A100 100 0 0 1 36.8 93.0 Z" fill="#b7cfe0"/>
      <path d="M0 0 L36.8 93.0 A100 100 0 0 1 12.5 99.2 Z" fill="#4a1760"/>
      <path d="M0 0 L12.5 99.2 A100 100 0 1 1 0 -100 Z" fill="#1d2f5e"/>
    </g>
    <text x="196" y="8" font-weight="700">HARRIS</text>
    <text x="196" y="16" font-weight="700">15,287</text>
    <text x="196" y="24">54% Discharge</text>
    <text x="196" y="32">46% Supervision</text>
    <text x="322" y="54" font-weight="700">DALLAS</text>
    <text x="322" y="62" font-weight="700">7,432</text>
    <text x="322" y="70">47% Discharge</text>
    <text x="322" y="78">53% Supervision</text>
    <text x="330" y="112" font-weight="700">TARRANT</text>
    <text x="330" y="120">5,132</text>
    <text x="330" y="128">46% Discharge</text>
    <text x="330" y="136">54% Supervision</text>
    <text x="266" y="158" font-weight="700">BEXAR</text>
    <text x="266" y="166">4,681</text>
    <text x="266" y="174">47% Discharge</text>
    <text x="266" y="182">53% Supervision</text>
    <text x="190" y="158" font-weight="700">TRAVIS</text>
    <text x="190" y="166">2,872</text>
    <text x="190" y="174">58% Discharge</text>
    <text x="190" y="182">42% Supervision</text>
    <text x="6" y="42" font-weight="700">ALL OTHER</text>
    <text x="6" y="50" font-weight="700">COUNTIES</text>
    <text x="14" y="58">52%</text>
    <g transform="translate(0,134)">
      <rect x="0.5" y="0.5" width="106" height="64" fill="#fff" stroke="#999" stroke-width="0.6"/>
      <rect x="4" y="4" width="5" height="5" fill="#7b1a1a"/><text x="12" y="9">Harris - 21%</text>
      <rect x="4" y="14" width="5" height="5" fill="#2e7d5b"/><text x="12" y="19">Dallas - 10%</text>
      <rect x="4" y="24" width="5" height="5" fill="#e4e4e4" stroke="#999" stroke-width="0.4"/><text x="12" y="29">Tarrant - 7%</text>
      <rect x="4" y="34" width="5" height="5" fill="#b7cfe0"/><text x="12" y="39">Bexar - 6%</text>
      <rect x="4" y="44" width="5" height="5" fill="#4a1760"/><text x="12" y="49">Travis - 4%</text>
      <rect x="4" y="54" width="5" height="5" fill="#1d2f5e"/><text x="12" y="59">All Other Counties - 52%</text>
    </g>
  </svg>
  <a class="fig-caption">Figure 1</a>

  <div class="footer-mark"></div>
  <div class="footer-band"></div>
  <div class="page-no">Page 2</div>
</div>
</body>
</html>
```